IT Company needs a Wordpress Web Design

We need a wordpress website for a new IT Company called 'RJ Systemworks'. We develop educational software for Middle and High School Students and Staff. Our initial product is DeskRoute - a web app that allows School Counselors to track information about the students that they see. We would like to see modern designs that include the company logo and the DeskRoute logo

Target Market(s)

Educators

Industry/Entity Type

Information Technology

Coding

Coded - Design and coding required

Number of Pages Required

1 page

Font styles to use
Sans Serif

Requirements
Must have
• Must be able to use WordPress
Should not have
• No Flash

```html
<!DOCTYPE html>
<html lang="en">
<head>
<meta charset="utf-8">
<title>RJ Systemworks</title>
<link href="https://fonts.googleapis.com/css2?family=Lato:wght@900&family=Open+Sans:wght@400;600&family=Roboto:wght@400;500&display=swap" rel="stylesheet">
<style>
:root{
  --blue:#4a86c3;
  --blue-dark:#3f76b0;
  --accent:#3f80c4;
  --pale:#e6f0fb;
  --ink:#222;
  --body:#555;
  --muted:#888;
  --line:#cfcfcf;
  --white:#fff;
  --foot-bar:#e9eff7;
}
*{margin:0;padding:0;box-sizing:border-box}
html,body{width:1200px;height:3396px;overflow:hidden;background:var(--white)}
body{position:relative;font-family:"Open Sans",Arial,sans-serif;color:var(--body)}
.abs{position:absolute}
.topbar{left:0;top:0;width:1200px;height:50px;background:var(--blue);color:var(--white);font-size:15px}
.topbar .mail{left:712px;top:16px;display:flex;align-items:center;gap:8px}
.topbar .sep{left:942px;top:8px;width:1px;height:34px;background:rgba(255,255,255,.6)}
.topbar .phone{left:962px;top:12px;display:flex;align-items:center;gap:10px;font-size:22px}
.nav{left:0;top:50px;width:1200px;height:68px;background:var(--white);border-bottom:1px solid #eee}
.nav a{position:absolute;top:22px;font-family:"Roboto",sans-serif;font-size:17px;color:#333;text-decoration:none}
.nav a.active{color:var(--accent)}
.brand{left:68px;top:11px;width:140px;height:95px;background:var(--white);border:3px solid var(--blue);display:flex;flex-direction:column;align-items:center;justify-content:center;gap:6px}
.brand .mark{width:22px;height:22px;background:var(--blue)}
.brand span{font-family:"Roboto",sans-serif;font-weight:500;font-size:17px;color:var(--blue);text-align:center;line-height:1.1}
.hero{left:0;top:118px;width:1200px;height:568px;background:linear-gradient(90deg,#8a7a66 0%,#c9b59b 35%,#d8cbb8 65%,#b8a48a 100%)}
.hero h1{position:absolute;right:80px;top:186px;font-family:"Lato",sans-serif;font-weight:900;font-size:41px;color:#111;white-space:nowrap}
.hero p{position:absolute;right:80px;top:236px;text-align:right;font-size:21px;line-height:29px;color:#111}
.btn-outline{display:flex;align-items:center;justify-content:center;background:var(--white);border:2px solid #333;font-family:"Open Sans",sans-serif;font-size:18px;color:#111}
.hero .btn-outline{position:absolute;left:905px;top:307px;width:215px;height:46px}
.section-title{width:1200px;left:0;text-align:center;font-family:"Roboto",sans-serif;font-weight:400;font-size:40px;color:var(--ink)}
.section-title em{font-style:normal;color:var(--accent)}
.welcome-text{left:80px;top:800px;width:400px;font-size:15px;line-height:23px;color:var(--body)}
.photo{background:linear-gradient(135deg,#c9cfd6,#8c97a3)}
.welcome-photo{left:525px;top:804px;width:593px;height:312px}
.promise{left:80px;top:962px;width:581px;height:245px;background:var(--blue)}
.promise .frame{position:absolute;left:42px;top:28px;width:503px;height:191px;border:1px solid rgba(255,255,255,.8)}
.promise .frame i{position:absolute;width:8px;height:8px;border:1px solid var(--white);border-radius:50%;background:var(--blue)}
.promise p{position:absolute;left:100px;top:44px;width:420px;font-size:31px;line-height:40px;color:var(--white)}
.products-photo{left:0;top:1290px;width:582px;height:403px;background:linear-gradient(90deg,#eef0f2,#d7dbe0)}
.products-intro{left:464px;top:1318px;width:656px;font-size:15px;line-height:23px;color:#999}
.faq{left:600px;top:1384px;width:520px;font-size:15px}
.faq .q{display:flex;align-items:center;gap:10px;color:var(--accent);height:41px}
.faq .q.open{color:#222}
.faq .q svg{flex:none}
.faq .a{font-size:15px;line-height:23px;color:#555;margin:-6px 0 14px}
.btn-blue{display:flex;align-items:center;justify-content:center;background:var(--blue);color:var(--white);font-family:"Roboto",sans-serif;font-size:20px}
.help{left:0;top:1698px;width:1200px;height:267px;background:linear-gradient(180deg,#5b93cc,#4a86c3 60%,#3f7ab8)}
.help h2{position:absolute;top:42px;width:1200px;text-align:center;font-family:"Roboto",sans-serif;font-weight:400;font-size:39px;color:var(--white)}
.help p{position:absolute;left:230px;top:104px;width:740px;text-align:center;font-size:15px;line-height:24px;color:var(--white)}
.help .btn-outline{position:absolute;top:167px;width:217px;height:48px;border:none}
.quote-panel{left:0;top:2133px;width:525px;height:414px;background:var(--pale)}
.quote-mark{left:76px;top:2190px}
.quote-text{left:131px;top:2210px;width:320px;font-size:15px;line-height:24px;color:#444}
.client-name{left:131px;top:2338px;font-family:"Roboto",sans-serif;font-weight:500;font-size:17px;color:var(--blue-dark)}
.client-role{left:131px;top:2370px;font-size:15px;color:var(--muted)}
.dots{left:278px;top:2427px;display:flex;gap:9px}
.dots i{width:11px;height:11px;border-radius:50%;border:1.5px solid var(--blue)}
.dots i.on{background:var(--blue-dark)}
.client-photo{left:525px;top:2083px;width:595px;height:414px;background:linear-gradient(135deg,#f1ece6,#cfc2b5)}
.touch-text{left:140px;top:2662px;width:920px;text-align:center;font-size:15px;line-height:25px}
.field{border-bottom:1px solid var(--line);font-size:14px;color:#555;padding-left:12px}
.field-msg{left:197px;top:2806px;width:808px;height:85px}
.submit{left:512px;top:2903px;width:176px;height:45px}
.footer{left:0;top:3002px;width:1200px;height:342px;background:linear-gradient(135deg,#5a94cf,#4a86c3 50%,#5a8fc6)}
.footer h4{position:absolute;top:48px;font-family:"Roboto",sans-serif;font-weight:400;font-size:18px;color:var(--white)}
.footer ul{position:absolute;list-style:none;top:88px;font-size:14px;line-height:24px;color:var(--white)}
.footer ul li::before{content:"›";margin-right:8px}
.contact-list{position:absolute;left:344px;top:90px;font-size:15px;color:var(--white)}
.contact-list div{display:flex;gap:10px;align-items:flex-start;margin-bottom:14px;line-height:22px}
.news-text{position:absolute;left:614px;top:90px;width:220px;font-size:14px;line-height:22px;color:var(--white)}
.news-email{position:absolute;left:614px;top:155px;width:220px;height:46px;border:1px solid rgba(255,255,255,.8);background:rgba(255,255,255,.08);color:var(--white);font-size:14px;line-height:20px;padding:12px}
.news-btn{position:absolute;left:614px;top:214px;width:178px;height:48px;background:var(--white);color:#222;font-size:18px;display:flex;align-items:center;justify-content:center}
.social{position:absolute;left:910px;display:flex;align-items:center;gap:18px;font-size:15px;color:var(--white)}
.social i{width:46px;height:46px;border:1px solid rgba(255,255,255,.8);background:rgba(255,255,255,.08)}
.copyright{left:0;top:3344px;width:1200px;height:52px;background:var(--foot-bar);text-align:center;line-height:52px;font-size:15px;color:#555}
.copyright b{color:var(--blue-dark);font-weight:600}
</style>
</head>
<body>

<header>
  <div class="abs topbar">
    <div class="abs mail">
      <svg width="18" height="13" viewBox="0 0 18 13"><rect x="0.5" y="0.5" width="17" height="12" fill="none" stroke="#fff"/><path d="M1 1l8 6 8-6" fill="none" stroke="#fff"/></svg>
      hello@rjsystemworks.com
    </div>
    <div class="abs sep"></div>
    <div class="abs phone">
      <svg width="18" height="18" viewBox="0 0 24 24"><path d="M6.6 10.8a15 15 0 006.6 6.6l2.2-2.2a1 1 0 011-.25 11.4 11.4 0 003.6.6 1 1 0 011 1V20a1 1 0 01-1 1A17 17 0 013 4a1 1 0 011-1h3.5a1 1 0 011 1 11.4 11.4 0 00.6 3.6 1 1 0 01-.25 1z" fill="#fff"/></svg>
      555 010 7878
    </div>
  </div>
  <nav class="abs nav">
    <a class="active" style="left:588px">Home</a>
    <a style="left:705px">About</a>
    <a style="left:820px">Products</a>
    <a style="left:960px">FAQ</a>
    <a style="left:1060px">Contact</a>
  </nav>
  <div class="abs brand"><div class="mark"></div><span>RJ Systemworks</span></div>
</header>

<section class="abs hero" role="img" aria-label="Photo of a student sitting with a laptop beside stone columns">
  <h1>STUDENTS HAVE A DIGITAL LIFE</h1>
  <p>Lorem ipsum dolor sit amet, consectetur adipiscing elit.<br>Sed dictum, ante ut dictum lacinia, ante.</p>
  <div class="btn-outline">GET A FREE QUOTE</div>
</section>

<h2 class="abs section-title" style="top:732px">Welcome to <em>RJ Systemworks</em></h2>
<p class="abs welcome-text">Lorem Ipsum is simply dummy text of the printing and typesetting industry. Lorem Ipsum has been the industry's standard dummy text ever since the 1500s, when an unknown printer took a galley of type and scrambled it to make a type specimen book.</p>
<div class="abs photo welcome-photo" role="img" aria-label="Photo of two colleagues in a business meeting"></div>
<div class="abs promise">
  <div class="frame">
    <i style="left:-5px;top:-5px"></i><i style="right:-5px;top:-5px"></i>
    <i style="left:-5px;bottom:-5px"></i><i style="right:-5px;bottom:-5px"></i>
  </div>
  <p>With our specialists, and experts at your disposal, you will face complex HR issues with confidence</p>
</div>

<h2 class="abs section-title" style="top:1253px;left:60px">Our <em>Products</em></h2>
<div class="abs products-photo" role="img" aria-label="Photo of a young schoolgirl sitting on the floor with a laptop"></div>
<p class="abs products-intro">Lorem Ipsum has been the industry's standard dummy text ever since the 1500s, when an unknown printer took a galley.</p>
<div class="abs faq">
  <div class="q open"><svg width="16" height="16"><rect x="1" y="7" width="14" height="2" fill="#333"/></svg>What is DeskRoute ?</div>
  <p class="a">DeskRoute is an electronic sign in system that replaces your old - fashioned clipboard.</p>
  <div class="q"><svg width="16" height="16"><rect x="1" y="7" width="14" height="2" fill="#666"/><rect x="7" y="1" width="2" height="14" fill="#666"/></svg>Why should I buy DeskRoute ?</div>
  <div class="q"><svg width="16" height="16"><rect x="1" y="7" width="14" height="2" fill="#666"/><rect x="7" y="1" width="2" height="14" fill="#666"/></svg>How much does it cost ?</div>
  <div class="q"><svg width="16" height="16"><rect x="1" y="7" width="14" height="2" fill="#666"/><rect x="7" y="1" width="2" height="14" fill="#666"/></svg>Who can view information in DeskRoute ?</div>
</div>
<div class="abs btn-blue" style="left:600px;top:1598px;width:220px;height:46px">VIEW ALL</div>

<section class="abs help" role="img" aria-label="Blue tinted photo of a classroom">
  <h2>We are here to help you!</h2>
  <p>Lorem Ipsum is simply dummy text of the printing and typesetting industry. Lorem Ipsum has been the industry's standard dummy text ever since the 1500.</p>
  <div class="btn-outline" style="left:369px">GET A FREE QUOTE</div>
  <div class="btn-outline" style="left:609px">GET PRICING</div>
</section>

<h2 class="abs section-title" style="top:2012px">Client's <em>happy Words</em></h2>
<div class="abs quote-panel"></div>
<svg class="abs quote-mark" width="34" height="28" viewBox="0 0 34 28"><path d="M0 14Q0 2 12 0v5Q6 7 6 12h6v16H0zM20 14Q20 2 32 0v5Q26 7 26 12h6v16H20z" fill="#b9c7d6"/></svg>
<p class="abs quote-text">"Lorem Ipsum is simply dummy text of the printing and typesetting industry. Lorem Ipsum has been the industry's standard dummy text ever since the 1500s."</p>
<div class="abs client-name">- Client's Name</div>
<div class="abs client-role">Manage,LNB Company</div>
<div class="abs dots"><i class="on"></i><i></i><i></i></div>
<div class="abs client-photo" role="img" aria-label="Photo of a smiling woman working on a laptop"></div>

<h2 class="abs section-title" style="top:2596px">Get in <em>Touch</em></h2>
<p class="abs touch-text">Lorem Ipsum is simply dummy text of the printing and typesetting industry. Lorem Ipsum has been the industry's standard dummy text ever since the 1500.</p>
<div class="abs field" style="left:197px;top:2744px;width:256px;height:32px">Name</div>
<div class="abs field" style="left:471px;top:2744px;width:258px;height:32px">Contact</div>
<div class="abs field" style="left:747px;top:2744px;width:258px;height:32px">E mail Id</div>
<div class="abs field field-msg">Message
  <svg style="position:absolute;right:14px;bottom:10px" width="14" height="14"><g fill="#888"><circle cx="12" cy="2" r="1.3"/><circle cx="8" cy="6" r="1.3"/><circle cx="12" cy="6" r="1.3"/><circle cx="4" cy="10" r="1.3"/><circle cx="8" cy="10" r="1.3"/><circle cx="12" cy="10" r="1.3"/></g></svg>
</div>
<div class="abs btn-blue submit">SUBMIT</div>

<footer class="abs footer" role="img" aria-label="Blue tinted photo of laptops on a desk">
  <h4 style="left:82px">Useful Links</h4>
  <ul style="left:82px"><li>Home</li><li>About us</li><li>Product</li><li>FAQ's</li><li>Testimonial</li><li>Contact Us</li></ul>
  <h4 style="left:344px">Get in touch</h4>
  <div class="contact-list">
    <div><svg width="14" height="18" viewBox="0 0 14 18"><path d="M7 0a7 7 0 017 7c0 5-7 11-7 11S0 12 0 7a7 7 0 017-7z" fill="#fff"/><circle cx="7" cy="7" r="2.5" fill="#4a86c3"/></svg><span>123,Lorem Ipsum,<br>Country,123456</span></div>
    <div><svg width="16" height="16" viewBox="0 0 24 24"><path d="M6.6 10.8a15 15 0 006.6 6.6l2.2-2.2a1 1 0 011-.25 11.4 11.4 0 003.6.6 1 1 0 011 1V20a1 1 0 01-1 1A17 17 0 013 4a1 1 0 011-1h3.5a1 1 0 011 1 11.4 11.4 0 00.6 3.6 1 1 0 01-.25 1z" fill="#fff"/></svg><span>555 010 7878</span></div>
    <div><svg width="16" height="16" viewBox="0 0 16 16"><rect x="1" y="4" width="14" height="11" rx="1" fill="#fff"/><rect x="4" y="1" width="8" height="4" fill="#fff"/><rect x="4" y="7" width="8" height="3" fill="#4a86c3"/></svg><span>555 010 1212</span></div>
    <div><svg width="18" height="13" viewBox="0 0 18 13"><rect x="0.5" y="0.5" width="17" height="12" fill="none" stroke="#fff"/><path d="M1 1l8 6 8-6" fill="none" stroke="#fff"/></svg><span>hello@rjsystemworks.com</span></div>
  </div>
  <h4 style="left:614px">NewsLetter</h4>
  <div class="news-text">Lorem Ipsum is simply dummy text of the printing.</div>
  <div class="news-email">Email</div>
  <div class="news-btn">SUBMIT</div>
  <h4 style="left:910px">Follow Us</h4>
  <div class="social" style="top:82px"><i></i>Facepage</div>
  <div class="social" style="top:142px"><i></i>Chirper</div>
  <div class="social" style="top:202px"><i></i>Linkwork</div>
</footer>
<div class="abs copyright">© <b>RJ Systemworks</b> - 2017 All Right Reserved.</div>

</body>
</html>
```